KestrelNet Business Cards

Create business cards for our exciting new software company. We provide cloud billing systems and provisioning software for campany that need monthly SaaS and Cloud Billing

Target Market(s)

Enterprise businesses, b2b, telecom carriers, software manufactures

Industry/Entity Type

Software

```html
<!DOCTYPE html>
<html lang="en">
<head>
<meta charset="utf-8">
<title>KestrelNet Business Cards</title>
<link rel="stylesheet" href="https://fonts.googleapis.com/css2?family=Open+Sans:wght@400;600;700&display=swap">
<style>
  :root {
    --backdrop: #3a3a3c;
    --card-top: #1f6088;
    --card-bottom: #154766;
    --card-edge: #0f3550;
    --accent: #a9dcef;
    --text-light: #e8f4fa;
    --text-soft: #cfe6f1;
  }
  * { margin: 0; padding: 0; box-sizing: border-box; }
  html, body {
    width: 1200px; height: 1023px; overflow: hidden;
    background: var(--backdrop);
    font-family: "Open Sans", Arial, sans-serif;
  }
  .canvas { position: relative; width: 1200px; height: 1023px; }
  .card {
    position: absolute;
    width: 525px; height: 300px;
    border-radius: 22px;
    background: linear-gradient(160deg, var(--card-top), var(--card-bottom));
    box-shadow: 0 4px 0 var(--card-edge), 0 14px 30px rgba(0,0,0,0.45);
    color: var(--text-light);
  }
  .card--front { left: 70px; top: 150px; }
  .card--back { left: 605px; top: 560px; }

  .brand { position: absolute; display: flex; align-items: center; gap: 10px; }
  .brand__dot { width: 16px; height: 16px; border-radius: 50%; background: var(--accent); }
  .brand__name { font-weight: 600; color: var(--accent); letter-spacing: 0.5px; line-height: 1; }
  .card--front .brand { right: 34px; top: 48px; }
  .card--front .brand__name { font-size: 40px; }
  .card--back .brand { right: 60px; top: 110px; }
  .card--back .brand__name { font-size: 52px; }
  .card--back .brand__dot { width: 20px; height: 20px; }

  .address {
    position: absolute; right: 34px; top: 168px; text-align: right;
    font-size: 14px; line-height: 1.55; color: var(--text-light);
  }
  .person { position: absolute; left: 34px; bottom: 30px; }
  .person__name { font-size: 21px; font-weight: 700; color: var(--accent); }
  .person__role { font-size: 14px; color: var(--text-light); margin-bottom: 10px; }
  .contact { list-style: none; font-size: 14px; line-height: 1.55; color: var(--text-soft); }
  .contact li { display: flex; align-items: center; gap: 9px; }
  .contact svg { width: 13px; height: 13px; fill: var(--text-light); flex: none; }
</style>
</head>
<body>
<main class="canvas">
  <section class="card card--front" aria-label="Business card front">
    <div class="brand"><span class="brand__dot"></span><span class="brand__name">KestrelNet</span></div>
    <div class="address">Somewhere Streetname Address<br>Cityname, CN 12345</div>
    <div class="person">
      <div class="person__name">Daniel Hartley</div>
      <div class="person__role">President &amp; CEO</div>
      <ul class="contact">
        <li><svg viewBox="0 0 16 16"><path d="M3 1h3l1 4-2 1c1 2 3 4 5 5l1-2 4 1v3c0 1-1 2-2 2C7 15 1 9 1 3c0-1 1-2 2-2z"/></svg>+0 000 000 0000</li>
        <li><svg viewBox="0 0 16 16"><path d="M4 0h8a1 1 0 0 1 1 1v14a1 1 0 0 1-1 1H4a1 1 0 0 1-1-1V1a1 1 0 0 1 1-1zm1 2v10h6V2z"/></svg>+0 000 000 0000</li>
        <li><svg viewBox="0 0 16 16"><path d="M1 3h14v10H1zm1 1.5V5l6 4 6-4v-.5z"/></svg>dhartley@kestrelnet.com</li>
        <li><svg viewBox="0 0 16 16"><path d="M8 1a7 7 0 1 0 0 14A7 7 0 0 0 8 1zm0 1.5c.8 1 1.4 2.5 1.5 4.5h-3c.1-2 .7-3.5 1.5-4.5zM2.6 9h2.4c.1 1.6.5 3 1.1 4A5.5 5.5 0 0 1 2.6 9zm0-2A5.5 5.5 0 0 1 6.1 3C5.5 4 5.1 5.4 5 7zm3.9 2h3c-.1 2-.7 3.5-1.5 4.5-.8-1-1.4-2.5-1.5-4.5zm3.4 4c.6-1 1-2.4 1.1-4h2.4a5.5 5.5 0 0 1-3.5 4zm1.1-6c-.1-1.6-.5-3-1.1-4a5.5 5.5 0 0 1 3.5 4z"/></svg>www.kestrelnet.com</li>
      </ul>
    </div>
  </section>

  <section class="card card--back" aria-label="Business card back">
    <div class="brand"><span class="brand__dot"></span><span class="brand__name">KestrelNet</span></div>
  </section>
</main>
</body>
</html>
```